"Maple Hollow" red wine label design

We are a Sydney based company. We need to design a wine label for a Australian red wine.
Front label include following info:
Our brand: "Maple Hollow";
Product name: "Shiraz 2016";
In the bottom with small font: "Wine of Australia", "750ml"
Back label:
the back label would need to be consistent with the front label, with space for one paragraph of tasting notes, and ingredient info etc.
we would like to use white, gold and blue in this label. It should make customer feel the magical and beautiful moment of starry night.

We also need a logo design for the wine brand: "Maple Hollow"

I have attached a few wine bottle that used blue to give you some inspirations.

We need the design in AI file format.

Target Market(s)

both men and women

Industry/Entity Type

It Company

Logo Text

Maple Hollow

Requirements
Nice to have
• gold borderline, words; use of blue and white

```html
<!DOCTYPE html>
<html lang="en">
<head>
<meta charset="utf-8">
<title>Maple Hollow – Shiraz 2016 Label</title>
<link rel="stylesheet" href="https://fonts.googleapis.com/css2?family=Mrs+Saint+Delafield&family=Montserrat:wght@400;700&display=swap">
<style>
  :root {
    --night: #08131f;
    --night-glow: #0e1e2c;
    --ridge-dark: #0d2b38;
    --ridge-mid: #335b6b;
    --ridge-light: #99b6bf;
    --mist: #d1dfda;
    --gold: #877550;
    --gold-soft: #a8966f;
  }
  html, body {
    margin: 0;
    padding: 0;
    width: 1200px;
    height: 2211px;
    overflow: hidden;
    background: var(--mist);
  }
  .label {
    position: relative;
    width: 1200px;
    height: 2211px;
    overflow: hidden;
    background: var(--mist);
  }
  .night-sky {
    position: absolute;
    left: 0;
    top: 0;
    width: 1200px;
    height: 1240px;
    background: radial-gradient(ellipse at 50% 35%, var(--night-glow) 0%, var(--night) 70%);
  }
  .mountain-scene {
    position: absolute;
    left: 0;
    top: 1060px;
    width: 1200px;
    height: 760px;
    background: linear-gradient(to bottom,
      var(--night) 0%,
      var(--ridge-dark) 12%,
      var(--ridge-dark) 30%,
      var(--ridge-mid) 48%,
      var(--ridge-mid) 62%,
      var(--ridge-light) 78%,
      var(--ridge-light) 92%,
      var(--mist) 100%);
  }
  .frame-outer {
    position: absolute;
    left: 29px;
    top: 29px;
    width: 1141px;
    height: 2151px;
    border: 1.5px solid var(--gold-soft);
    box-sizing: border-box;
  }
  .frame-inner {
    position: absolute;
    left: 46px;
    top: 47px;
    width: 1108px;
    height: 2117px;
    border: 5px solid var(--gold);
    box-sizing: border-box;
  }
  .brand-name {
    position: absolute;
    left: 0;
    top: 0;
    margin: 0;
    font-family: "Mrs Saint Delafield", cursive;
    font-weight: 400;
    color: var(--gold);
    line-height: 1;
    white-space: nowrap;
    transform: rotate(-8deg);
  }
  .brand-name span {
    display: block;
    position: absolute;
    font-size: 270px;
    -webkit-text-stroke: 1.5px var(--gold);
  }
  .brand-name .line-one {
    left: 110px;
    top: 520px;
  }
  .brand-name .line-two {
    left: 430px;
    top: 770px;
  }
  .product {
    position: absolute;
    left: 0;
    width: 1200px;
    text-align: center;
    font-family: "Montserrat", sans-serif;
    color: var(--gold);
  }
  .product-name {
    top: 1872px;
    margin: 0;
    font-size: 53px;
    font-weight: 700;
    letter-spacing: 0.5px;
  }
  .product-details {
    top: 1996px;
    margin: 0;
    font-size: 32px;
    font-weight: 400;
    line-height: 55px;
  }
</style>
</head>
<body>
  <main class="label">
    <div class="night-sky" role="img" aria-label="Deep navy night sky scattered with small white stars"></div>
    <div class="mountain-scene" role="img" aria-label="Layered mountain ranges fading from dark teal to pale misty blue"></div>

    <div class="frame-outer"></div>
    <div class="frame-inner"></div>

    <h1 class="brand-name" aria-label="Maple Hollow">
      <span class="line-one">Maple</span>
      <span class="line-two">Hollow</span>
    </h1>

    <h2 class="product product-name">Shiraz 2016</h2>
    <p class="product product-details">750ml<br>Wine of Australia</p>
  </main>
</body>
</html>
```